Harlow Auto , a Dealership and Repair Shop in Linford Iowa

Harlow Auto is a repair shop and auto sales dealership that offers oil changes, alignments, tires, air conditioning work, computer diagnostics. Focused on Vantras, Marlo and Brisk. Small business with less than 10 employees. Billboard sign is in town and not the larger billboard
billboard is 8ft x 18ft

Target Market(s)

General public

Industry/Entity Type

automotive

Font styles to use
Serif
Sans Serif

Colors

Designer to choose colors to be used in the design.

Requirements
Must have
• Located 2 miles north of Linford. Sales and service. Phone number 319-555-0187
Nice to have
• Picture of a car or truck, or both. picture of wrench
Should not have
• Not sure

```html
<!DOCTYPE html>
<html lang="en">
<head>
<meta charset="utf-8">
<title>Harlow Auto – Billboard</title>
<link href="https://fonts.googleapis.com/css2?family=Krona+One&display=swap" rel="stylesheet">
<style>
  :root {
    --stage: #9a9a9a;
    --blue-bright: #1f63f0;
    --blue-deep: #0a3cc0;
    --blue-ink: #0f3aa8;
    --white: #ffffff;
    --ink: #161616;
    --band-dark: #222222;
    --road: #d4d4d4;
  }
  * { margin: 0; padding: 0; box-sizing: border-box; }
  html, body { width: 1200px; height: 678px; overflow: hidden; }
  body { background: var(--stage); font-family: "Krona One", sans-serif; position: relative; }

  .billboard {
    position: absolute; left: 87px; top: 111px; width: 1026px; height: 456px;
    overflow: hidden; background: var(--white);
    box-shadow: 0 4px 14px rgba(0,0,0,.25);
  }
  .sky {
    position: absolute; left: 0; top: 0; width: 1026px; height: 253px;
    background:
      linear-gradient(115deg, rgba(255,255,255,.10) 0 18%, transparent 18% 26%, rgba(255,255,255,.07) 26% 34%, transparent 34%),
      linear-gradient(100deg, var(--blue-bright) 0%, var(--blue-deep) 75%, #0a3fbf 100%);
  }
  .sky-right {
    position: absolute; left: 700px; top: 253px; width: 326px; height: 60px;
    background: var(--blue-deep);
  }
  .road {
    position: absolute; left: 820px; top: 240px; width: 260px; height: 240px;
    background: var(--road); transform: skewX(-18deg);
  }
  .headline {
    position: absolute; left: 0; top: 30px; width: 675px; text-align: center;
    color: var(--white); font-weight: 400;
  }
  .headline .lead { font-size: 42px; line-height: 42px; letter-spacing: -1.5px; display: block; }
  .headline .main { font-size: 62px; line-height: 56px; letter-spacing: -3px; display: block; margin-top: 4px; }

  .tab {
    position: absolute; left: 73px; top: 206px; width: 416px; height: 48px;
  }
  .tab svg { position: absolute; inset: 0; }
  .tab span {
    position: relative; display: block; text-align: center; line-height: 48px;
    font-size: 26px; color: var(--blue-ink); letter-spacing: -0.5px;
  }

  .services {
    position: absolute; top: 274px; list-style: none; color: var(--ink);
    font-size: 22px; letter-spacing: -0.5px; line-height: 30px;
  }
  .services.left { left: 60px; }
  .services.right { left: 268px; }
  .services li { position: relative; padding-left: 19px; }
  .services li svg { position: absolute; left: 0; top: 9px; }

  .phone-band {
    position: absolute; left: 0; top: 378px; width: 1026px; height: 78px; background: var(--band-dark);
  }
  .phone {
    position: absolute; left: 54px; top: 385px; height: 64px; display: flex; align-items: center; gap: 12px;
    color: var(--white); font-size: 53px; letter-spacing: -2.5px;
  }

  .brand {
    position: absolute; left: 728px; top: 74px; width: 240px; text-align: center; color: var(--white);
  }
  .brand .name { font-size: 24px; letter-spacing: -0.5px; display: block; }
  .brand .town { font-size: 11px; display: block; margin-top: 10px; }

  .truck-photo {
    position: absolute; left: 609px; top: 157px; width: 420px; height: 280px;
    border-radius: 40px 20px 30px 40px;
    background: radial-gradient(ellipse at 45% 45%, #2f6fd4 0%, #1b4fa8 50%, #2a2d33 100%);
  }
</style>
</head>
<body>
  <div class="billboard">
    <div class="sky"></div>
    <div class="sky-right"></div>
    <div class="road"></div>

    <h1 class="headline">
      <span class="lead">LOCATED</span>
      <span class="main">2 MILES NORTH<br>OF LINFORD</span>
    </h1>

    <div class="tab">
      <svg width="416" height="48" viewBox="0 0 416 48"><polygon points="22,0 394,0 416,48 0,48" fill="#ffffff"/></svg>
      <span>SALES &amp; SERVICE</span>
    </div>

    <ul class="services left">
      <li><svg width="12" height="12" viewBox="0 0 12 12"><circle cx="6" cy="6" r="6" fill="#0f3aa8"/><path d="M3 6.2l2 2 4-4" stroke="#fff" stroke-width="1.6" fill="none"/></svg>Oil changes</li>
      <li><svg width="12" height="12" viewBox="0 0 12 12"><circle cx="6" cy="6" r="6" fill="#0f3aa8"/><path d="M3 6.2l2 2 4-4" stroke="#fff" stroke-width="1.6" fill="none"/></svg>Alignments</li>
      <li><svg width="12" height="12" viewBox="0 0 12 12"><circle cx="6" cy="6" r="6" fill="#0f3aa8"/><path d="M3 6.2l2 2 4-4" stroke="#fff" stroke-width="1.6" fill="none"/></svg>Tires</li>
    </ul>
    <ul class="services right">
      <li><svg width="12" height="12" viewBox="0 0 12 12"><circle cx="6" cy="6" r="6" fill="#0f3aa8"/><path d="M3 6.2l2 2 4-4" stroke="#fff" stroke-width="1.6" fill="none"/></svg>Air conditioning work</li>
      <li><svg width="12" height="12" viewBox="0 0 12 12"><circle cx="6" cy="6" r="6" fill="#0f3aa8"/><path d="M3 6.2l2 2 4-4" stroke="#fff" stroke-width="1.6" fill="none"/></svg>Computer<br>diagnostics</li>
    </ul>

    <div class="phone-band"></div>
    <div class="phone">
      <svg width="34" height="34" viewBox="0 0 32 32" aria-hidden="true">
        <circle cx="16" cy="16" r="16" fill="#ffffff"/>
        <path d="M11 8.5c1-.6 1.8-.3 2.3.6l1.3 2.5c.4.8.2 1.5-.5 2l-1 .8c.7 1.8 2.2 3.4 4 4.3l.9-1c.6-.6 1.3-.8 2-.4l2.5 1.4c.9.5 1.1 1.4.5 2.3l-.9 1.2c-.8 1-2.1 1.3-3.3.9-4.6-1.6-8-5.1-9.3-9.7-.3-1.2.1-2.5 1.1-3.2z" fill="#222222"/>
      </svg>
      <span>319-555-0187</span>
    </div>

    <div class="brand">
      <span class="name">HARLOW AUTO</span>
      <span class="town">Linford, IA</span>
    </div>

    <div class="truck-photo" role="img" aria-label="Photo of a blue full-size pickup truck, front three-quarter view"></div>
  </div>
</body>
</html>
```